Thank you for shopping with us business card

We would like a thank you card for our rebranded business. We used to be "Brindle Goods" but are now "Marlow Finds. Old thank you card and new logo will be attached for reference. New thank you card does not have to be same design as old thank you card, but please use new logo.
Shopmart URL is now marlowfinds.shopmart.example
Instagram is @Marlow_Finds
Email is marlowfinds@mailbox.example
Thank you!

Contact Information for Business Card

Shopmart site, email, Instagram

```html
<!DOCTYPE html>
<html lang="en">
<head>
<meta charset="utf-8">
<title>Marlow Finds – Thank You Card</title>
<link rel="stylesheet" href="https://fonts.googleapis.com/css2?family=Montserrat:wght@400;500;600;700;800&display=swap">
<style>
  :root {
    --ink: #463f5e;
    --ink-deep: #3d3653;
    --lavender: #e6e2f1;
    --paper: #ffffff;
    --stage: #2b2b2e;
    --muted: #5c566f;
  }
  * { box-sizing: border-box; margin: 0; padding: 0; }
  html, body { width: 1200px; height: 900px; overflow: hidden; }
  body {
    background: var(--stage);
    font-family: "Montserrat", sans-serif;
    display: flex;
    flex-direction: column;
    align-items: center;
    justify-content: center;
    gap: 56px;
  }
  .card {
    width: 560px;
    height: 320px;
    position: relative;
    overflow: hidden;
  }

  /* Front */
  .card-front {
    background: var(--ink);
    display: flex;
    align-items: center;
    justify-content: center;
  }
  .front-brand {
    display: flex;
    flex-direction: column;
    align-items: center;
    gap: 14px;
    color: var(--paper);
  }
  .front-mark {
    width: 58px; height: 58px;
    border-radius: 50%;
    background: var(--paper);
  }
  .front-name {
    font-weight: 600;
    font-size: 17px;
    letter-spacing: 1.5px;
    text-transform: uppercase;
  }

  /* Back */
  .card-back { background: var(--paper); color: var(--ink); }
  .top-wave { position: absolute; top: 0; left: 0; width: 100%; height: 34px; }
  .thanks {
    position: absolute;
    left: 46px; top: 48px;
  }
  .thanks-title {
    font-weight: 800;
    font-size: 66px;
    line-height: 0.95;
    letter-spacing: 0.5px;
  }
  .thanks-sub {
    font-weight: 700;
    font-size: 27px;
    letter-spacing: 1px;
    margin-top: 2px;
  }
  .thanks-note {
    font-weight: 600;
    font-size: 11.5px;
    letter-spacing: 0.6px;
    line-height: 1.45;
    margin-top: 12px;
    padding-left: 30px;
    color: var(--muted);
  }
  .contacts {
    position: absolute;
    left: 30px; top: 200px;
    list-style: none;
    display: flex; flex-direction: column; gap: 5px;
  }
  .contact {
    display: flex; align-items: center; gap: 9px;
    font-weight: 500;
    font-size: 15px;
    color: var(--ink);
  }
  .contact svg { width: 17px; height: 17px; flex: none; }
  .brand-lockup {
    position: absolute;
    right: 34px; top: 196px;
    display: flex; align-items: center; gap: 16px;
  }
  .lockup-mark {
    width: 40px; height: 40px;
    border-radius: 50%;
    background: var(--ink);
  }
  .lockup-divider { width: 1px; height: 58px; background: var(--ink); }
  .lockup-name {
    font-weight: 600;
    font-size: 18px;
    line-height: 1.15;
    letter-spacing: 1px;
    text-transform: uppercase;
  }
  .review-band {
    position: absolute;
    left: 0; bottom: 0;
    width: 100%; height: 34px;
    background: var(--ink);
    color: var(--paper);
    font-weight: 500;
    font-size: 12px;
    letter-spacing: 1px;
    text-transform: uppercase;
    display: flex; align-items: center; justify-content: flex-end;
    padding-right: 48px;
  }
</style>
</head>
<body>

  <section class="card card-front" aria-label="Card front">
    <div class="front-brand">
      <span class="front-mark" aria-hidden="true"></span>
      <span class="front-name">Marlow Finds</span>
    </div>
  </section>

  <section class="card card-back" aria-label="Card back">
    <svg class="top-wave" viewBox="0 0 560 34" preserveAspectRatio="none" aria-hidden="true">
      <path d="M0 0 H560 V14 C520 20 500 8 460 14 C420 20 400 26 350 20 C300 14 280 24 230 22 C180 20 150 30 100 26 C60 23 30 30 0 28 Z" fill="var(--lavender)"/>
    </svg>

    <div class="thanks">
      <h1 class="thanks-title">THANK YOU</h1>
      <p class="thanks-sub">FOR YOUR PURCHASE</p>
      <p class="thanks-note">YOUR PURCHASE MADE MY DAY AND<br>I HOPE THIS PACKAGE BRIGHTENS YOURS.</p>
    </div>

    <ul class="contacts">
      <li class="contact">
        <svg viewBox="0 0 20 20" aria-hidden="true"><circle cx="10" cy="10" r="8.5" fill="none" stroke="var(--ink)" stroke-width="1.6"/><ellipse cx="10" cy="10" rx="3.6" ry="8.5" fill="none" stroke="var(--ink)" stroke-width="1.3"/><line x1="1.5" y1="10" x2="18.5" y2="10" stroke="var(--ink)" stroke-width="1.3"/></svg>
        marlowfinds.shopmart.example
      </li>
      <li class="contact">
        <svg viewBox="0 0 20 20" aria-hidden="true"><circle cx="10" cy="10" r="8.5" fill="var(--ink)"/></svg>
        @Marlow_Finds
      </li>
      <li class="contact">
        <svg viewBox="0 0 20 20" aria-hidden="true"><rect x="2" y="5" width="16" height="11" fill="none" stroke="var(--ink)" stroke-width="1.6"/><path d="M2 5 L10 11 L18 5" fill="none" stroke="var(--ink)" stroke-width="1.6"/></svg>
        marlowfinds@mailbox.example
      </li>
    </ul>

    <div class="brand-lockup">
      <span class="lockup-mark" aria-hidden="true"></span>
      <span class="lockup-divider" aria-hidden="true"></span>
      <span class="lockup-name">Marlow<br>Finds</span>
    </div>

    <div class="review-band">Please come back and leave a review</div>
  </section>

</body>
</html>
```